The Kestrowe Banner Ad

The Kestrowe (www.thekestrowe.example) is a news-based website in South China that also features dining and nightlife listings, events, jobs, classifieds and more. The cities we cover are Guangzhou and Shenzhen. We have the rare opportunity to have an advertisement placed on the website of the leading English newspaper in Asia. It is a captive audience of people already reading news, so we want to draw their attention to an alternative site for information.

The ad copy is:

Want more China?
The latest news, dining, nightlife, and jobs.
Guangzhou and Shenzhen
The Kestrowe (with a button saying "Check it out")

(Or something like that... you have freedom to adjust the wording).

The dimensions are 300 x 250 px, with a file size <30kb in JPEG/Animated GIF.

```html
<!DOCTYPE html>
<html lang="en">
<head>
<meta charset="utf-8">
<title>The Kestrowe Banner Ad</title>
<link rel="stylesheet" href="https://fonts.googleapis.com/css2?family=Source+Sans+3:wght@400;600;700&display=swap">
<style>
  :root {
    --stage: #2a2a2a;
    --night-top: #10185a;
    --night-mid: #2b2550;
    --night-low: #3d2a36;
    --glow: #a0502a;
    --ink: #141a3a;
    --paper: #ffffff;
    --button: #c4100e;
    --button-edge: #8e0a09;
    --band-red: #780b0b;
    --band-grey: rgba(150, 150, 150, 0.55);
    --band-black: #050505;
  }
  * { box-sizing: border-box; margin: 0; padding: 0; }
  html, body {
    width: 1200px; height: 768px; overflow: hidden;
    background: var(--stage);
    font-family: "Source Sans 3", "Myriad Pro", Arial, sans-serif;
  }
  .banner-row {
    position: absolute; left: 0; top: 0;
    width: 1200px; height: 768px;
  }
  .banner {
    position: absolute; top: 241px;
    width: 300px; height: 250px;
    transform: scale(1.115); transform-origin: 0 0;
    overflow: hidden;
    box-shadow: 0 3px 10px rgba(0,0,0,0.6);
    color: var(--paper);
    text-align: center;
  }
  .banner--red { left: 82px; }
  .banner--glass { left: 433px; }
  .banner--black { left: 782px; }

  .city-photo {
    position: absolute; left: 0; top: 0; width: 300px; height: 250px;
    background:
      radial-gradient(ellipse 160px 40px at 60px 170px, rgba(220,110,50,0.45), transparent),
      radial-gradient(ellipse 140px 50px at 240px 150px, rgba(200,60,80,0.35), transparent),
      linear-gradient(180deg, var(--night-top) 0%, var(--night-mid) 35%, var(--night-low) 60%, var(--glow) 78%, #2a1a20 100%);
  }
  .banner--red .city-photo { height: 200px; }
  .banner--black .city-photo { height: 235px; }

  .bottom-band { position: absolute; left: 0; width: 300px; }
  .banner--red .bottom-band { top: 200px; height: 50px; background: var(--band-red); }
  .banner--glass .bottom-band { top: 200px; height: 42px; background: var(--band-grey); }
  .banner--black .bottom-band { top: 230px; height: 20px; background: var(--band-black); }

  .brand-name {
    position: absolute; left: 0; right: 0; top: 12px;
    font-size: 24px; font-weight: 600; letter-spacing: 0.3px;
    color: var(--paper);
  }
  .headline {
    position: absolute; left: 29px; top: 74px;
    width: 245px; height: 34px;
    background: var(--paper); color: var(--ink);
    font-size: 24px; font-weight: 700; line-height: 34px;
    letter-spacing: -0.3px;
  }
  .tagline {
    position: absolute; left: 40px; right: 40px; top: 127px;
    font-size: 13.5px; font-weight: 600; line-height: 17px;
    text-shadow: 0 1px 2px rgba(0,0,0,0.7);
  }
  .cta {
    position: absolute; left: 99px; top: 209px;
    width: 108px; height: 29px;
    background: var(--button);
    border-bottom: 3px solid var(--button-edge);
    border-radius: 2px;
    font-size: 14px; font-weight: 400; line-height: 27px;
    color: var(--paper);
  }
  .banner--glass .cta, .banner--black .cta { left: 98px; top: 204px; }
</style>
</head>
<body>
<main class="banner-row">
  <section class="banner banner--red">
    <div class="city-photo" role="img" aria-label="Night skyline of a Chinese city with glowing streets"></div>
    <div class="bottom-band"></div>
    <div class="brand-name">The Kestrowe</div>
    <h1 class="headline">WANT MORE CHINA?</h1>
    <p class="tagline">The latest news, dining, nightlife, and jobs in Guangzhou and Shenzhen</p>
    <div class="cta">Check it out</div>
  </section>

  <section class="banner banner--glass">
    <div class="city-photo" role="img" aria-label="Night skyline of a Chinese city with glowing streets"></div>
    <div class="bottom-band"></div>
    <div class="brand-name">The Kestrowe</div>
    <h1 class="headline">WANT MORE CHINA?</h1>
    <p class="tagline">The latest news, dining, nightlife, and jobs in Guangzhou and Shenzhen</p>
    <div class="cta">Check it out</div>
  </section>

  <section class="banner banner--black">
    <div class="city-photo" role="img" aria-label="Night skyline of a Chinese city with glowing streets"></div>
    <div class="bottom-band"></div>
    <div class="brand-name">The Kestrowe</div>
    <h1 class="headline">WANT MORE CHINA?</h1>
    <p class="tagline">The latest news, dining, nightlife, and jobs in Guangzhou and Shenzhen</p>
    <div class="cta">Check it out</div>
  </section>
</main>
</body>
</html>
```